Natural Organic soap need packaging design

we need a packaging design for new company based in New Zealand Called 'Tellum Global ltd'.. We manufacture Natural organic soap bars.our main USP is that this soap is made of all natural ingredient and no chemical used and soap is made in New Zealand,so we need a design which look natural,simple,classy and luxury and packaging should reflect that its made in New Zealand.please find attached photos of sample soap.
soap will be in two variant:
1. Pure Manuka Honey soap
2. Goat Milk soap
NOTE: the soap in picture is not actually our soap its just a sample what our soap will look like so please don't make a design with FRAKKK written on it. TELLUM is the soap name.
Target Market(s)
international market. mainly young and kids
Industry/Entity Type
It Company
Look and feel

```html
<!DOCTYPE html>
<html lang="en">
<head>
<meta charset="utf-8">
<title>Tellum Pure Manuka Honey Soap – Carton Dieline</title>
<link rel="stylesheet" href="https://fonts.googleapis.com/css2?family=Montserrat:wght@400;500;600&display=swap">
<style>
  :root {
    --page-bg: #ffffff;
    --dieline-edge: #9b9b9b;
    --tuck-flap: #f6d778;
    --back-panel: #e3a62b;
    --end-panel: #f3b41f;
    --dust-flap: #f5b81d;
    --side-strip: #f6ba1c;
    --front-panel: #eeae1f;
    --honeycomb: #fbd35a;
    --ink-light: #ffffff;
    --ink-dark: #5a3d05;
  }
  html, body {
    margin: 0;
    padding: 0;
    width: 1200px;
    height: 853px;
    overflow: hidden;
    background: var(--page-bg);
  }
  .dieline {
    display: block;
    width: 1200px;
    height: 853px;
    font-family: "Montserrat", Arial, sans-serif;
  }
  .edge { fill: none; stroke: var(--dieline-edge); stroke-width: 5; stroke-linejoin: round; }
  .tuck-flap { fill: var(--tuck-flap); }
  .back-panel { fill: var(--back-panel); }
  .end-panel { fill: var(--end-panel); }
  .dust-flap { fill: var(--dust-flap); }
  .side-strip { fill: var(--side-strip); }
  .front-panel { fill: var(--front-panel); }
  .honeycomb-area { fill: var(--honeycomb); opacity: 0.35; }
  .front-frame { fill: none; stroke: var(--ink-light); stroke-width: 1.6; }
  .brand-name { fill: var(--ink-light); font-weight: 600; letter-spacing: 0.04em; }
  .product-name { fill: var(--ink-light); font-weight: 500; }
  .fine-print { fill: var(--ink-dark); font-weight: 400; font-size: 4.6px; }
  .net-weight { fill: var(--ink-dark); font-weight: 500; font-size: 5.2px; }
  .back-brand { fill: var(--ink-light); font-weight: 600; font-size: 15px; letter-spacing: 0.04em; }
</style>
</head>
<body>
<svg class="dieline" viewBox="-175 0 850 604" xmlns="http://www.w3.org/2000/svg" aria-label="Tellum Pure Manuka Honey Soap carton, flat dieline">

  <!-- outer cut line -->
  <g class="cut-outline">
    <path class="edge" d="M148,50 L152,24 Q153,22 156,22 L300,22 Q303,22 304,24 L307,50 Z"/>
    <rect class="edge" x="148" y="50" width="252" height="182"/>
    <rect class="edge" x="92" y="55" width="56" height="177"/>
    <path class="edge" d="M92,60 L48,60 Q36,60 36,72 L36,216 Q36,228 48,228 L92,228 Z"/>
    <rect class="edge" x="92" y="232" width="308" height="76"/>
    <rect class="edge" x="148" y="308" width="252" height="180"/>
    <path class="edge" d="M400,310 L452,310 Q465,310 465,323 L465,470 Q465,483 452,483 L400,483 Z"/>
    <path class="edge" d="M92,488 L400,488 L400,560 L104,560 Q92,560 92,548 Z"/>
  </g>

  <!-- tuck flap -->
  <path class="tuck-flap" d="M148,50 L152,24 Q153,22 156,22 L300,22 Q303,22 304,24 L307,50 Z"/>

  <!-- back panel -->
  <rect class="back-panel" x="148" y="50" width="252" height="182"/>
  <g class="back-copy" transform="rotate(180 274 141)">
    <text class="back-brand" x="158" y="72">TELLUM</text>
    <g class="ingredients-short">
      <text class="fine-print" x="158" y="88">Ingredients: Honey, olive</text>
      <text class="fine-print" x="158" y="95">oil, coconut oil, water,</text>
      <text class="fine-print" x="158" y="102">shea butter, cocoa butter,</text>
      <text class="fine-print" x="158" y="109">oat milk. Naturally</text>
      <text class="fine-print" x="158" y="116">scented with pure</text>
      <text class="fine-print" x="158" y="123">essential oils. Suitable</text>
      <text class="fine-print" x="158" y="130">for all skin types and</text>
      <text class="fine-print" x="158" y="137">gentle on young skin.</text>
      <text class="fine-print" x="158" y="144">No parabens, no SLS.</text>
      <text class="fine-print" x="158" y="151">Cruelty free formula.</text>
    </g>
    <g class="ingredients-full">
      <text class="fine-print" x="250" y="104">Ingredients: Sodium olivate, sodium cocoate,</text>
      <text class="fine-print" x="250" y="111">aqua, manuka honey, glycerin, shea butter,</text>
      <text class="fine-print" x="250" y="118">beeswax, kaolin clay, oat kernel flour, and</text>
      <text class="fine-print" x="250" y="125">a blend of natural plant oils and extracts.</text>
      <text class="fine-print" x="250" y="132">Gently cleanses and softens the skin while</text>
      <text class="fine-print" x="250" y="139">honey helps keep in natural moisture. Made</text>
      <text class="fine-print" x="250" y="146">in small batches with no harsh chemicals.</text>
      <text class="fine-print" x="250" y="153">Directions: Lather with warm water, apply</text>
      <text class="fine-print" x="250" y="160">to face and body, then rinse well. Store in</text>
      <text class="fine-print" x="250" y="167">a dry place between uses. Avoid the eyes.</text>
      <text class="fine-print" x="250" y="174">For external use only. Keep from children.</text>
      <text class="fine-print" x="250" y="181">Made with care in New Zealand.</text>
    </g>
    <text class="net-weight" x="340" y="222">Net. Wt: 80 mg</text>
  </g>

  <!-- left end panel and dust flap -->
  <path class="dust-flap" d="M92,60 L48,60 Q36,60 36,72 L36,216 Q36,228 48,228 L92,228 Z"/>
  <rect class="end-panel" x="92" y="55" width="56" height="177"/>
  <text class="brand-name" font-size="22" transform="translate(97 68) rotate(90)">TELLUM</text>
  <text class="product-name" font-size="11" transform="translate(127 68) rotate(90)">Pure Manuka Honey Soap</text>

  <!-- top side strip -->
  <rect class="side-strip" x="92" y="232" width="308" height="76"/>
  <rect class="honeycomb-area" x="318" y="236" width="80" height="68" rx="4" role="img" aria-label="faint honeycomb pattern"/>
  <text class="brand-name" x="164" y="278" font-size="25">TELLUM</text>
  <text class="product-name" x="290" y="266" font-size="13">Pure Manuka</text>
  <text class="product-name" x="290" y="284" font-size="13">Honey Soap</text>

  <!-- front panel -->
  <rect class="front-panel" x="148" y="308" width="252" height="180"/>
  <path class="front-frame" d="M170,320 L378,320 Q378,330 388,330 L388,466 Q378,466 378,476 L170,476 Q170,466 160,466 L160,330 Q170,330 170,320 Z"/>
  <text class="product-name" x="274" y="355" font-size="13" text-anchor="middle">Pure Manuka Honey Soap</text>
  <text class="brand-name" x="274" y="414" font-size="42" text-anchor="middle">TELLUM</text>

  <!-- right end panel -->
  <path class="end-panel" d="M400,310 L452,310 Q465,310 465,323 L465,470 Q465,483 452,483 L400,483 Z"/>
  <text class="product-name" font-size="11" transform="translate(410 320) rotate(90)">Pure Manuka Honey Soap</text>
  <text class="brand-name" font-size="20" transform="translate(438 336) rotate(90)">TELLUM</text>

  <!-- bottom side strip -->
  <path class="side-strip" d="M92,488 L400,488 L400,560 L104,560 Q92,560 92,548 Z"/>
  <rect class="honeycomb-area" x="280" y="492" width="86" height="64" rx="4" role="img" aria-label="faint honeycomb pattern"/>
  <text class="brand-name" x="164" y="532" font-size="25">TELLUM</text>
  <text class="product-name" x="290" y="520" font-size="13">Pure Manuka</text>
  <text class="product-name" x="290" y="538" font-size="13">Honey Soap</text>
</svg>
</body>
</html>
```